1200mm high x 900mm wide kids fitness poster for gym

I need an a poster designed to promote my kids/teenagers class.

This class is aimed at parents with kids between 10-15.

Design should be friendly and modern

Class is designed for kids that play sport and want to improve their fitness

Industry/Entity Type

Fitness

Font styles to use
Sans Serif

Colors

Designer to choose colors to be used in the design.

Requirements
Must have
• Text:
• Bold Stride teens program (TITLE)
• Improve: Performance, health, fitness, confidence, team mentality (BULLET POINTS)
• They will love our teen program! Contact us now to find out more:
• 1300524196
• enquiries@boldstride.fitness
• www.boldstride.fitness
• Must have friendly image of kids fitness or sport (FUN AND FRIENDLY IMAGE)

```html
<!DOCTYPE html>
<html lang="en">
<head>
<meta charset="utf-8">
<title>Bold Stride Teens Program Poster</title>
<link rel="stylesheet" href="https://fonts.googleapis.com/css2?family=Dosis:wght@400;500;600;700;800&display=swap">
<style>
  :root {
    --backdrop: #e9e8e6;
    --lime: #dde22c;
    --green: #6cb42e;
    --green-dark: #5aa126;
    --navy: #173f8c;
    --red: #e3202a;
    --purple: #4a1f8e;
    --ink: #222222;
    --white: #ffffff;
    --photo-sky: #5e9bd6;
    --photo-warm: #b8463a;
  }
  html, body {
    margin: 0;
    padding: 0;
    width: 1200px;
    height: 1148px;
    overflow: hidden;
    background: var(--backdrop);
  }
  .poster {
    position: absolute;
    left: 187px;
    top: 24px;
    width: 825px;
    height: 1100px;
    box-shadow: 0 6px 24px rgba(0,0,0,0.18);
  }
  .poster svg { display: block; width: 100%; height: 100%; }
  .poster text { font-family: 'Dosis', sans-serif; }
  .brand { font-weight: 800; fill: var(--navy); font-size: 26px; letter-spacing: 0.5px; }
  .badge-text { font-weight: 600; fill: var(--white); font-size: 30px; }
  .title-top { font-weight: 600; fill: var(--navy); font-size: 62px; }
  .title-bottom { font-weight: 600; fill: var(--red); font-size: 62px; }
  .improve-label { font-weight: 500; fill: var(--white); font-size: 22px; letter-spacing: 0.5px; }
  .benefits { font-weight: 400; fill: var(--ink); font-size: 23px; }
  .tagline { font-weight: 700; fill: var(--purple); font-size: 22px; }
  .contact-lead { font-weight: 700; fill: var(--ink); font-size: 15px; }
  .phone { font-weight: 700; fill: var(--purple); font-size: 44px; letter-spacing: 1px; }
  .web { font-weight: 700; fill: var(--purple); font-size: 14px; }
</style>
</head>
<body>
<div class="poster">
  <svg viewBox="0 0 600 800" xmlns="http://www.w3.org/2000/svg">
    <defs>
      <linearGradient id="photoTone" x1="0" y1="0" x2="1" y2="1">
        <stop offset="0" stop-color="var(--photo-sky)"/>
        <stop offset="0.55" stop-color="var(--photo-warm)"/>
        <stop offset="1" stop-color="#3c4a3a"/>
      </linearGradient>
      <clipPath id="sheet"><rect width="600" height="800"/></clipPath>
    </defs>
    <g clip-path="url(#sheet)">
      <rect class="field-lime" width="600" height="800" fill="var(--lime)"/>
      <path class="field-green" d="M355 0 H600 V390 C560 400 520 380 470 395 C430 405 395 380 390 340 C385 300 420 270 400 230 C380 190 330 170 340 110 C350 60 330 30 355 0 Z" fill="var(--green)"/>
      <path class="field-white" d="M0 430 C60 400 110 420 160 435 C220 452 260 440 300 420 C360 392 420 410 470 410 C530 410 570 395 600 400 V800 H0 Z" fill="var(--white)"/>
      <path class="blob-lime" d="M0 690 C40 670 90 665 140 672 C200 680 250 700 262 740 C272 775 255 800 240 800 H0 Z" fill="var(--lime)"/>
      <path class="blob-green" d="M356 800 C350 760 350 720 378 690 C410 660 470 650 520 652 C565 654 590 668 600 680 V800 Z" fill="var(--green)"/>

      <ellipse cx="190" cy="245" rx="148" ry="158" fill="var(--green)"/>
      <ellipse cx="190" cy="245" rx="140" ry="150" fill="url(#photoTone)" role="img" aria-label="Photo of two smiling kids in helmets and harnesses riding a zip line together"/>

      <circle cx="258" cy="48" r="12" fill="var(--navy)"/>
      <text class="brand" x="280" y="57">BOLD STRIDE</text>

      <circle cx="427" cy="213" r="92" fill="var(--purple)"/>
      <circle cx="427" cy="213" r="82" fill="none" stroke="var(--white)" stroke-width="3"/>
      <text class="badge-text" x="427" y="207" text-anchor="middle">COME JOIN</text>
      <text class="badge-text" x="427" y="238" text-anchor="middle">WITH US !</text>

      <text class="title-top" x="98" y="465">BOLD STRIDE</text>
      <text class="title-bottom" x="105" y="523">TEENS PROGRAM</text>

      <rect x="112" y="553" width="106" height="33" rx="16.5" fill="var(--red)"/>
      <text class="improve-label" x="165" y="577" text-anchor="middle">IMPROVE</text>
      <text class="benefits" x="239" y="563">Performance | Health | Fitness</text>
      <text class="benefits" x="239" y="588">Confidence | Team mentality</text>

      <rect x="112" y="605" width="410" height="34" rx="17" fill="var(--lime)"/>
      <text class="tagline" x="317" y="630" text-anchor="middle">THEY WILL LOVE OUR TEEN PROGRAM !</text>

      <text class="contact-lead" x="322" y="676" text-anchor="middle">CONTACT US NOW TO FIND OUT MORE</text>
      <text class="phone" x="322" y="725" text-anchor="middle">1300524196</text>
      <text class="web" x="330" y="750" text-anchor="middle">WWW.BOLDSTRIDE.FITNESS</text>
      <text class="web" x="330" y="768" text-anchor="middle">ENQUIRIES@BOLDSTRIDE.FITNESS</text>
    </g>
  </svg>
</div>
</body>
</html>
```